Calendar Ad / Flyer

Our law firm needs a calendar ad to place in a local calendar.
THE DEADLINE IS THIS THURSDAY 06/28/2018.

Attached is the ad used in last years calendar. A few notes on this...
**. This is by no means the model to follow.
Please be creative and do what makes more sense marketing wise.
1. Need to update the color scheme which corresponds to the new website at morvanlegal.net
2. The "MORVAN LEGAL | STANDING FIRM FOR YOUR FUTURE" should be put at the top and made larger
3. "KNOWN AND TRUSTED IN OUR COMMUNITY FOR OVER 21 YEARS" should be changed to "KNOWN AND TRUSTED IN OUR COMMUNITY FOR OVER 22 YEARS"
4. "Dorian K. Morvan, Esq." should be made larger and better positioned.
5. Under the list of practices, it should be changed to have:
"Personal Injury, Legal Malpractice, Unlicensed Contractors, Medical Malpractice, Civil Litigation"
6. Contact information (i.e. contact number, website, and address) should be better positioned
7. Placement of endorsement logos should stand out more.
8. New picture of head attorney is attached.

Last but not least... Give it your best shot!

```html
<!DOCTYPE html>
<html lang="en">
<head>
<meta charset="utf-8">
<title>Morvan Legal – Calendar Ad</title>
<link rel="stylesheet" href="https://fonts.googleapis.com/css2?family=Montserrat:wght@500;700;800&family=Roboto:wght@400;500&display=swap">
<style>
  :root {
    --navy: #0d3a5a;
    --sky: #1aa6e0;
    --sand: #ede5da;
    --gold: #b9955a;
    --white: #ffffff;
    --ink: #23313d;
    --badge-red: #8e1b1b;
    --badge-crimson: #d32323;
    --badge-olive: #7b6a3a;
    --badge-blue: #1a72b8;
    --badge-teal: #2d8fc4;
  }
  * { margin: 0; padding: 0; box-sizing: border-box; }
  html, body { width: 1200px; height: 881px; overflow: hidden; background: #f2f2f2; }
  .ad {
    position: relative; width: 1200px; height: 881px; overflow: hidden;
    background: var(--white); font-family: "Roboto", sans-serif; color: var(--navy);
  }
  .ad-shapes { position: absolute; inset: 0; }
  .headline-band {
    position: absolute; left: 0; top: 0; width: 100%; height: 95px;
    display: flex; align-items: center; padding-left: 56px;
    font-family: "Montserrat", sans-serif; font-weight: 800; font-size: 36px;
    color: var(--white); letter-spacing: 0.5px;
  }
  .brand { position: absolute; left: 150px; top: 160px; width: 640px; }
  .brand-name {
    display: flex; align-items: center; gap: 18px;
    font-family: "Montserrat", sans-serif; font-weight: 800; font-size: 56px;
    letter-spacing: 4px; color: var(--navy); line-height: 1; white-space: nowrap;
  }
  .brand-mark { width: 44px; height: 44px; background: var(--gold); flex: none; }
  .brand-tagline {
    margin-top: 16px; margin-left: 62px;
    font-family: "Montserrat", sans-serif; font-weight: 700; font-size: 21px;
    letter-spacing: 2px; color: var(--sky); white-space: nowrap;
  }
  .practices {
    position: absolute; left: 70px; top: 360px; width: 720px;
    font-size: 30px; font-weight: 500; line-height: 1.35; color: var(--navy);
  }
  .attorney-name {
    position: absolute; left: 70px; top: 478px;
    font-family: "Montserrat", sans-serif; font-weight: 500; font-size: 62px;
    color: var(--gold); white-space: nowrap;
  }
  .contact-web {
    position: absolute; left: 470px; top: 614px;
    display: flex; align-items: center; gap: 14px;
    font-size: 30px; color: var(--white);
  }
  .contact-phone {
    position: absolute; left: 80px; top: 664px;
    display: flex; align-items: center; gap: 16px;
    font-size: 34px; font-weight: 500; color: var(--white); letter-spacing: 1px;
  }
  .contact-address {
    position: absolute; left: 60px; top: 770px;
    display: flex; align-items: center; gap: 18px;
    font-size: 20px; line-height: 1.4; color: var(--ink); white-space: nowrap;
  }
  .contact-address address { font-style: normal; }
  .endorsements {
    position: absolute; left: 455px; top: 762px; height: 56px;
    display: flex; align-items: center; gap: 16px;
  }
  .badge { flex: none; }
  .badge-seal { width: 46px; height: 46px; border-radius: 50%; background: var(--badge-red); }
  .badge-rating { width: 58px; height: 36px; border-radius: 4px; background: var(--badge-crimson); }
  .badge-list { width: 50px; height: 44px; background: var(--badge-olive); }
  .badge-accredited { width: 72px; height: 30px; border-radius: 4px; background: var(--badge-blue); }
  .badge-score { width: 48px; height: 48px; border-radius: 50%; background: var(--badge-teal); }
  .attorney-photo {
    position: absolute; left: 830px; top: 120px; width: 330px; height: 761px;
    background: linear-gradient(180deg, #d8d8d8 0%, #8f9194 35%, #7a7c80 70%, #6c6e72 100%);
  }
</style>
</head>
<body>
<main class="ad">
  <svg class="ad-shapes" width="1200" height="881" viewBox="0 0 1200 881" aria-hidden="true">
    <rect class="sand-band" x="0" y="95" width="1200" height="235" fill="var(--sand)"/>
    <rect class="navy-band" x="0" y="0" width="1200" height="95" fill="var(--navy)"/>
    <polygon class="sky-corner" points="0,95 150,95 0,265" fill="var(--sky)"/>
    <polygon class="gold-band" points="0,652 262,652 302,600 1200,600 1200,690 620,690 580,735 0,735" fill="var(--gold)"/>
  </svg>

  <div class="headline-band">Known And Trusted In Our Community For Over 22 Years</div>

  <div class="brand">
    <div class="brand-name"><span class="brand-mark"></span>MORVAN LEGAL</div>
    <div class="brand-tagline">STANDING FIRM FOR YOUR FUTURE</div>
  </div>

  <p class="practices">Personal Injury • Legal Malpractice • Unlicensed Contractors • Medical Malpractice • Civil Litigation</p>

  <h1 class="attorney-name">Dorian K. Morvan, Esq.</h1>

  <div class="contact-web">
    <svg width="32" height="32" viewBox="0 0 32 32" aria-hidden="true" fill="none" stroke="#fff" stroke-width="2">
      <circle cx="16" cy="16" r="13"/><ellipse cx="16" cy="16" rx="6" ry="13"/>
      <line x1="3" y1="16" x2="29" y2="16"/><line x1="5" y1="9" x2="27" y2="9"/><line x1="5" y1="23" x2="27" y2="23"/>
    </svg>
    morvanlegal.net
  </div>

  <div class="contact-phone">
    <svg width="38" height="38" viewBox="0 0 38 38" aria-hidden="true" fill="none" stroke="#fff" stroke-width="2.4" stroke-linejoin="round">
      <path d="M9 5l6 7-3 4c2 4 6 8 10 10l4-3 7 6-4 5C17 33 5 21 5 9z"/>
      <path d="M22 6a11 11 0 0 1 10 10M22 12a5 5 0 0 1 4 4"/>
    </svg>
    (888) 555-0142
  </div>

  <div class="contact-address">
    <svg width="28" height="38" viewBox="0 0 30 40" aria-hidden="true" fill="none" stroke="var(--ink)" stroke-width="2">
      <path d="M15 38C6 26 3 20 3 14a12 12 0 0 1 24 0c0 6-3 12-12 24z"/><circle cx="15" cy="14" r="5"/>
    </svg>
    <address>2180 Larchmont Ave., Suite #340<br>Westbrook, CA 90417</address>
  </div>

  <div class="endorsements">
    <span class="badge badge-seal"></span>
    <span class="badge badge-rating"></span>
    <span class="badge badge-list"></span>
    <span class="badge badge-accredited"></span>
    <span class="badge badge-score"></span>
  </div>

  <div class="attorney-photo" role="img" aria-label="Photo of the head attorney standing in a grey suit with a blue tie"></div>
</main>
</body>
</html>
```